Commercial Construction Interior Fitout company needs Logo and Business Cards

We need a logo and business card design. We specialise in Commercial Ceilings, Partitions, Plastering and Carpentry.

Company name: 7QX Commercial Interiors. Would like a professional looking card more than a fancy look. Gloss front preferably black pattern with Fluro Green and white text.

Will need:

Name
Position
Phone
Fax
Email
Postal Address
Web address
Updates

Thank you so much everyone for your efforts and fantastic designs..   If I didn't respond to everyone personally,  my apologises. 

Again, thanks all

R.M                               

Target Market(s)

Existing & New clients in the Construction Industry

Industry/Entity Type

Business

Requirements
Nice to have
• 7QX to be overlapped or made into some sort of Logo

```html
<!DOCTYPE html>
<html lang="en">
<head>
<meta charset="utf-8">
<title>7QX Commercial Interiors – Business Card</title>
<link rel="stylesheet" href="https://fonts.googleapis.com/css2?family=Michroma&family=Arimo:wght@400;700&display=swap">
<style>
  :root {
    --canvas: #ffffff;
    --card-white: #fbfbfb;
    --card-black: #1d1d1f;
    --card-black-deep: #111112;
    --fluro: #7ed321;
    --fluro-deep: #3fae2a;
    --ink: #1a1a1a;
    --text-light: #f2f2f2;
    --text-muted: #d8d8d8;
    --divider: #6a6a6a;
  }
  * { box-sizing: border-box; margin: 0; padding: 0; }
  html, body {
    width: 1200px; height: 900px; overflow: hidden;
    background: var(--canvas);
  }
  .stage {
    position: relative; width: 1200px; height: 900px;
    display: flex; align-items: center; justify-content: center; gap: 50px;
  }
  .card {
    position: relative; width: 530px; height: 310px;
    border-radius: 22px; overflow: hidden;
    box-shadow: 0 10px 28px rgba(0,0,0,.18);
  }

  /* Contact side */
  .card--contact { background: var(--card-white); }
  .card__brand {
    position: absolute; left: 32px; top: 48px;
    display: flex; align-items: center; gap: 16px;
  }
  .brand-square {
    width: 44px; height: 44px; background: var(--fluro-deep);
  }
  .brand-name {
    font-family: "Michroma", sans-serif; font-size: 21px;
    color: var(--ink); letter-spacing: .3px;
  }
  .card__stripe {
    position: absolute; left: 0; right: 0; top: 146px; height: 7px;
    background: linear-gradient(90deg, var(--fluro-deep), var(--fluro));
  }
  .card__panel {
    position: absolute; left: 0; right: 0; top: 153px; bottom: 0;
    background: linear-gradient(180deg, var(--card-black) 0%, var(--card-black-deep) 100%);
  }
  .person {
    position: absolute; right: 362px; top: 28px; text-align: right;
    font-family: "Arimo", sans-serif;
  }
  .person__name { color: var(--fluro); font-size: 15px; }
  .person__role { color: var(--text-light); font-size: 12px; margin-top: 4px; }
  .panel__divider {
    position: absolute; left: 184px; top: 18px; bottom: 30px;
    width: 1px; background: var(--divider);
  }
  .contact-list {
    position: absolute; left: 200px; top: 22px; list-style: none;
    font-family: "Arimo", sans-serif; font-size: 14.5px;
    color: var(--text-light); line-height: 19px;
  }
  .contact-list li { display: flex; align-items: flex-start; gap: 5px; }
  .contact-list svg { width: 15px; height: 15px; flex: none; margin-top: 2px; fill: var(--fluro); }

  /* Brand side */
  .card--brand {
    background: radial-gradient(ellipse at 50% 40%, #2a2a2c 0%, var(--card-black) 55%, var(--card-black-deep) 100%);
    display: flex; flex-direction: column; align-items: center; justify-content: center; gap: 34px;
  }
  .brand-square--large { width: 110px; height: 110px; }
  .brand-name--large {
    font-family: "Michroma", sans-serif; font-size: 22px;
    color: var(--text-muted); letter-spacing: .4px;
  }
</style>
</head>
<body>
<main class="stage">

  <section class="card card--contact" aria-label="Business card, contact side">
    <div class="card__brand">
      <span class="brand-square"></span>
      <span class="brand-name">7QX Commercial Interiors</span>
    </div>
    <div class="card__stripe"></div>
    <div class="card__panel">
      <div class="person">
        <p class="person__name">Dane Holloway</p>
        <p class="person__role">Manager</p>
      </div>
      <div class="panel__divider"></div>
      <ul class="contact-list">
        <li>
          <svg viewBox="0 0 16 16" aria-hidden="true"><path d="M3.5 1.5l2.5 0 1 3.5-1.7 1.2a8 8 0 0 0 4.5 4.5L11 9l3.5 1v2.5c0 1-1 2-2 2C6.5 14.5 1.5 9.5 1.5 3.5c0-1 1-2 2-2z"/></svg>
          <span>555-014-2271</span>
        </li>
        <li>
          <svg viewBox="0 0 16 16" aria-hidden="true"><path d="M4 1h6l2 2v3H4z"/><path d="M1.5 7h13v6.5h-13zM4 9v1.5h8V9z"/></svg>
          <span>555-014-2298</span>
        </li>
        <li>
          <svg viewBox="0 0 16 16" aria-hidden="true"><path d="M1 3h14v10H1zM2.5 4.5v.4L8 8.8l5.5-3.9v-.4z"/></svg>
          <span>7qxcommercial@mailbox.com</span>
        </li>
        <li>
          <svg viewBox="0 0 16 16" aria-hidden="true"><path d="M8 1a7 7 0 1 0 0 14A7 7 0 0 0 8 1zm0 1.5c.8 0 1.7 1.7 2 4.5H6c.3-2.8 1.2-4.5 2-4.5zM2.6 7h2a13 13 0 0 1 .5-3.8A5.5 5.5 0 0 0 2.6 7zm8.8 0h2a5.5 5.5 0 0 0-2.5-3.8A13 13 0 0 1 11.4 7zM2.6 9a5.5 5.5 0 0 0 2.5 3.8A13 13 0 0 1 4.6 9zm3.4 0c.3 2.8 1.2 4.5 2 4.5s1.7-1.7 2-4.5zm5.4 0a13 13 0 0 1-.5 3.8A5.5 5.5 0 0 0 13.4 9z"/></svg>
          <span>www.7qxcommercial.com</span>
        </li>
        <li>
          <svg viewBox="0 0 16 16" aria-hidden="true"><path d="M8 1.5l7 6.2-1 1.1-1-.9V14.5H9.5v-4h-3v4H3V7.9l-1 .9-1-1.1z"/></svg>
          <span>4870 N. Ridgeline Highway,<br>Ashford, CO 80990</span>
        </li>
      </ul>
    </div>
  </section>

  <section class="card card--brand" aria-label="Business card, brand side">
    <span class="brand-square brand-square--large"></span>
    <span class="brand-name--large">7QX Commercial Interiors</span>
  </section>

</main>
</body>
</html>
```